Business Card for staff member of football club FC Brenor

I would like to get a business card template for all staff member of our soccer club.

The card should use as much as possible the 2 colors of the club : Red which is the main color and blue which is the alternative color. It can be balanced between the two like our logo.

I prefer simple and lean design.

Contact Information for Business Card

Bussiness card should have all main stuff as describe here below in must have.

Font styles to use
Sans Serif

Requirements
Must have
• Name : Mathieu DERLAPIN
Fonction : Président
Mobile : +41 xx xxx xx xx
Email : first.lastname@fcbrenor.example
Adresse of the club : FC Brenor, 4820 Brenor
Website of the club : www.fcbrenor.example
Nice to have
• Version with and without picture of the staff member

A version for men, a version for women staff member.

```html
<!DOCTYPE html>
<html lang="fr">
<head>
<meta charset="utf-8">
<title>FC Brenor – Business Card</title>
<link rel="stylesheet" href="https://fonts.googleapis.com/css2?family=Roboto+Condensed:wght@400;700&family=Open+Sans:wght@400&display=swap">
<style>
  :root {
    --stage: #e9e9eb;
    --ink: #231f20;
    --white: #ffffff;
    --red-dark: #b91d27;
    --red-light: #e4252a;
    --blue-light: #1a88c9;
    --blue-dark: #0b5a86;
    --grey-dark: #d2d3d5;
    --grey-light: #f8f8f8;
  }
  * { margin: 0; padding: 0; box-sizing: border-box; }
  html, body { width: 1200px; height: 1200px; overflow: hidden; }
  body {
    background: var(--stage);
    position: relative;
    font-family: "Roboto Condensed", sans-serif;
  }
  .card {
    position: absolute;
    left: 207px;
    width: 850px;
    height: 512px;
    overflow: hidden;
  }
  .card-front { top: 48px; }
  .card-back {
    top: 635px;
    background: linear-gradient(90deg, var(--white) 0%, var(--grey-dark) 100%);
  }

  /* Front: left grey panel */
  .side-panel {
    position: absolute; left: 0; top: 0;
    width: 280px; height: 100%;
    background: linear-gradient(90deg, var(--grey-dark) 0%, var(--grey-light) 100%);
  }
  .photo-frame {
    position: absolute; left: 72px; top: 112px;
    width: 137px; height: 137px;
    border: 3px solid #000;
    display: flex; align-items: center; justify-content: center;
    font-family: "Open Sans", sans-serif;
    font-size: 23px; color: var(--ink);
  }
  .club-mark {
    position: absolute; left: 0; top: 300px;
    width: 280px;
    display: flex; flex-direction: column; align-items: center; gap: 10px;
  }
  .club-mark .dot {
    width: 56px; height: 56px; border-radius: 50%;
    background: var(--red-light);
  }
  .club-mark .name {
    font-size: 24px; font-weight: 700; color: var(--ink);
  }

  .accent-strip {
    position: absolute; left: 280px; top: 0;
    width: 28px; height: 100%;
    background: linear-gradient(90deg, var(--blue-light) 0%, var(--blue-light) 45%, var(--blue-dark) 100%);
  }
  .info-panel {
    position: absolute; left: 308px; top: 0; right: 0; height: 100%;
    background: linear-gradient(90deg, var(--red-dark) 0%, var(--red-light) 100%);
    color: var(--white);
  }
  .person-name {
    position: absolute; left: 41px; top: 101px;
    font-size: 52px; font-weight: 400; letter-spacing: 0.2px; line-height: 1;
    white-space: nowrap;
  }
  .person-role {
    position: absolute; left: 41px; top: 158px;
    font-size: 29px; line-height: 1;
  }
  .contact-list { list-style: none; }
  .contact-item {
    position: absolute; left: 34px;
    display: flex; align-items: center;
    font-size: 26px; line-height: 1; white-space: nowrap;
  }
  .contact-item svg { width: 30px; height: 30px; margin-right: 18px; flex: none; }
  .contact-phone { top: 234px; }
  .contact-mail  { top: 283px; }
  .contact-addr  { top: 338px; }
  .contact-web   { top: 390px; }

  /* Back */
  .back-mark {
    position: absolute; left: 0; top: 0; width: 100%; height: 100%;
    display: flex; align-items: center; justify-content: center; gap: 14px;
  }
  .back-mark .dot {
    width: 52px; height: 52px; border-radius: 50%;
    background: var(--red-light);
  }
  .back-mark .name {
    font-size: 60px; font-weight: 700; color: var(--ink); line-height: 1;
  }
</style>
</head>
<body>

<section class="card card-front" aria-label="Recto de la carte">
  <div class="side-panel">
    <div class="photo-frame">Photo</div>
    <div class="club-mark">
      <span class="dot"></span>
      <span class="name">FC Brenor</span>
    </div>
  </div>
  <div class="accent-strip"></div>
  <div class="info-panel">
    <h1 class="person-name">Mathieu DERLAPIN</h1>
    <p class="person-role">Président</p>
    <ul class="contact-list">
      <li class="contact-item contact-phone">
        <svg viewBox="0 0 30 30" aria-hidden="true"><rect x="9" y="3" width="12" height="24" rx="3" fill="#fff"/><rect x="11.5" y="7" width="7" height="6" fill="#c8202a"/><circle cx="15" cy="21" r="1.6" fill="#c8202a"/></svg>
        +41 xx xxx xx xx
      </li>
      <li class="contact-item contact-mail">
        <svg viewBox="0 0 30 30" aria-hidden="true"><rect x="3" y="7" width="24" height="16" fill="none" stroke="#fff" stroke-width="2"/><path d="M3 7 L15 17 L27 7 M3 23 L12 14 M27 23 L18 14" fill="none" stroke="#fff" stroke-width="2"/></svg>
        first.lastname@fcbrenor.example
      </li>
      <li class="contact-item contact-addr">
        <svg viewBox="0 0 30 30" aria-hidden="true"><path d="M2 15 L15 3 L28 15" fill="none" stroke="#fff" stroke-width="3"/><path d="M6 14 V27 H24 V14" fill="none" stroke="#fff" stroke-width="3"/><rect x="12" y="19" width="6" height="8" fill="#fff"/></svg>
        FC Brenor, 4820 Brenor
      </li>
      <li class="contact-item contact-web">
        <svg viewBox="0 0 30 30" aria-hidden="true"><circle cx="13" cy="13" r="11" fill="none" stroke="#fff" stroke-width="2.5"/><path d="M2 13 H24 M13 2 V24 M5 7 H21 M5 19 H21" fill="none" stroke="#fff" stroke-width="1.8"/><path d="M16 14 L26 23 L21 23 L23 28 L21 29 L19 24 L16 27 Z" fill="#fff" stroke="#c8202a" stroke-width="1"/></svg>
        www.fcbrenor.example
      </li>
    </ul>
  </div>
</section>

<section class="card card-back" aria-label="Verso de la carte">
  <div class="back-mark">
    <span class="dot"></span>
    <span class="name">FC Brenor</span>
  </div>
</section>

</body>
</html>
```